Pell's Pot Labelling Project

We are a small fudge manufacturer based in Auckland, New Zealand and we're looking to revamp the look of our tubs in order to present a more professional looking product to the market and increase distribution. See our website @ www.pellsweets.co.nz to get a feel for our company and the fudge we make.

We have a number of flavours currently, and initial thoughts were to keep the labelling around the side of the tub uniform with the aim of keeping costs and inventory low, and allowing us to move into an In-Mould Label sooner as volumes grow. We're also looking for a top label which we envisaged as the method of identifying the flavour.
With the plan to move to IML in the future, and keeping costs low, the number of colours must also be taken into consideration.

The tubs we're planning to move to are the below dimensions:
Tub Height: 40 mm
Tub Circumference (bottom): 260 mm
Tub Circumference (top): 290 mm
Top Lid: 90 mm diameter

I've attached some images below:
- the tub
- our logo (we're happy to review the font used)
- our current label

Requirements
Must have
• - Room on the side for nutritional information & ingredient list (will differ by flavour)
- The words "Gluten Free" displayed.
- The words "Spoonable Fudge"
- The website address: www.pellsweets.co.nz
- Room for barcode (will differ by flavour)
Nice to have
• - Standard size stickers, so do not require customisation when printing.
- Easily applied stickers (taking into consideration the angled walls of the tub)
- Eye-catching
- Fun, but premium look and feel

```html
<!DOCTYPE html>
<html lang="en">
<head>
<meta charset="utf-8">
<title>Pell's Pot – Lid Labels</title>
<link rel="stylesheet" href="https://fonts.googleapis.com/css2?family=Source+Sans+3:wght@400;600;700&family=Tinos&display=swap">
<style>
  :root {
    --page: #ffffff;
    --ink-light: #ffffff;
    --cocoa: #231e19;
    --teal: #27b5c6;
    --berry: #8a0b55;
    --ring-dash: #7fd3e0;
    --brand-dot: #e94b7c;
    --photo-light: #a89584;
    --photo-dark: #6e6660;
  }
  * { box-sizing: border-box; margin: 0; padding: 0; }
  html, body {
    width: 1200px; height: 420px; overflow: hidden;
    background: var(--page);
    font-family: "Source Sans 3", "Helvetica Neue", Arial, sans-serif;
  }
  .label-sheet { position: relative; width: 1200px; height: 420px; }

  .lid-label {
    position: absolute; top: 12px;
    width: 392px; height: 392px; border-radius: 50%;
    overflow: hidden; color: var(--ink-light);
    background: var(--flavour);
  }
  .lid-label--crumbla { left: 4px; --flavour: var(--cocoa); }
  .lid-label--mochaberry { left: 404px; --flavour: var(--teal); }
  .lid-label--cocoanutta { left: 804px; --flavour: var(--berry); }

  .lid-label__ring {
    position: absolute; inset: 7px; border-radius: 50%;
    border: 1.5px solid var(--ink-light);
  }
  .lid-label__cutline {
    position: absolute; inset: 14px; border-radius: 50%;
    border: 1px dashed var(--ring-dash);
  }

  .lid-label__photo {
    position: absolute; left: 112px; top: 170px;
    width: 200px; height: 116px; border-radius: 50%;
    background: radial-gradient(ellipse at 50% 45%, var(--photo-light) 0%, var(--photo-dark) 100%);
  }

  .lid-label__claim {
    position: absolute; top: 38px; left: 0; width: 100%;
    text-align: center; font-size: 10px; font-weight: 400;
  }
  .brand {
    position: absolute; top: 58px; left: 0; width: 100%;
    display: flex; justify-content: center; align-items: center; gap: 8px;
  }
  .brand__dot { width: 26px; height: 26px; border-radius: 50%; background: var(--brand-dot); }
  .brand__name { font-size: 42px; font-weight: 700; line-height: 1; }

  .flavour-bar {
    position: absolute; top: 131px; height: 32px; left: 180px; right: -4px;
    border: 2px solid var(--ink-light); border-right: none;
    display: flex; align-items: center; background: var(--flavour);
  }
  .flavour-bar--dairy-free { left: 114px; }
  .flavour-bar__free {
    background: var(--ink-light); color: var(--flavour);
    font-size: 11px; font-weight: 600; line-height: 1.05;
    height: 100%; width: 60px; padding: 3px 4px;
  }
  .flavour-bar__name {
    font-size: 28px; font-weight: 400; line-height: 1; padding-left: 10px;
    white-space: nowrap; position: relative; z-index: 1;
  }
  .flavour-bar__tail {
    flex: 1; align-self: stretch; background: var(--ink-light);
    clip-path: polygon(14px 18%, 100% 18%, 100% 82%, 0 82%);
    margin-left: 10px;
  }

  .product-type__lead {
    position: absolute; top: 273px; left: 84px;
    font-size: 21px; font-weight: 400; line-height: 1;
  }
  .product-type__main {
    position: absolute; top: 292px; left: 0; width: 100%;
    text-align: center; font-size: 44px; font-weight: 400; line-height: 1;
  }

  .lid-label__web {
    position: absolute; top: 338px; left: 0; width: 100%;
    text-align: center; font-family: "Tinos", "Times New Roman", serif; font-size: 13px;
  }
</style>
</head>
<body>
<main class="label-sheet">

  <section class="lid-label lid-label--crumbla">
    <div class="lid-label__photo" role="img" aria-label="Photo of a spoon holding a scoop of fudge"></div>
    <div class="lid-label__ring"></div>
    <div class="lid-label__cutline"></div>
    <p class="lid-label__claim">Gluten Free</p>
    <div class="brand"><span class="brand__dot"></span><span class="brand__name">Pell's Pot</span></div>
    <div class="flavour-bar">
      <span class="flavour-bar__name">Crumbla</span><span class="flavour-bar__tail"></span>
    </div>
    <p class="product-type"><span class="product-type__lead">Spoonable</span><span class="product-type__main">Fudge</span></p>
    <p class="lid-label__web">www.pellsweets.co.nz</p>
  </section>

  <section class="lid-label lid-label--mochaberry">
    <div class="lid-label__photo" role="img" aria-label="Photo of a spoon holding a scoop of fudge"></div>
    <div class="lid-label__ring"></div>
    <div class="lid-label__cutline"></div>
    <p class="lid-label__claim">Gluten Free</p>
    <div class="brand"><span class="brand__dot"></span><span class="brand__name">Pell's Pot</span></div>
    <div class="flavour-bar flavour-bar--dairy-free">
      <span class="flavour-bar__free">Dairy<br>Free</span>
      <span class="flavour-bar__name">Mochaberry</span><span class="flavour-bar__tail"></span>
    </div>
    <p class="product-type"><span class="product-type__lead">Spoonable</span><span class="product-type__main">Fudge</span></p>
    <p class="lid-label__web">www.pellsweets.co.nz</p>
  </section>

  <section class="lid-label lid-label--cocoanutta">
    <div class="lid-label__photo" role="img" aria-label="Photo of a spoon holding a scoop of fudge"></div>
    <div class="lid-label__ring"></div>
    <div class="lid-label__cutline"></div>
    <p class="lid-label__claim">Gluten Free</p>
    <div class="brand"><span class="brand__dot"></span><span class="brand__name">Pell's Pot</span></div>
    <div class="flavour-bar flavour-bar--dairy-free">
      <span class="flavour-bar__free">Dairy<br>Free</span>
      <span class="flavour-bar__name">Cocoanutta</span><span class="flavour-bar__tail"></span>
    </div>
    <p class="product-type"><span class="product-type__lead">Spoonable</span><span class="product-type__main">Fudge</span></p>
    <p class="lid-label__web">www.pellsweets.co.nz</p>
  </section>

</main>
</body>
</html>
```